Surface Protection company needs cards

We are a New Zealand company that will apply nanotechnology coatings on surfaces to prevent growth and spread of bacteria, viruses, mold etc with a sprayer. We deal with large corporates, airlines, hospitals and schools so we are after a new modern, simple and clean look that will have great visual impact.
We a company that is focused on prevention and protection.

Company name, Vela Shield

Subtext, Antimicrobial Surface Protection

Logo, VS

Target Market(s)

Hospitals, Transport agencies, Airlines, Corporate entities

Contact Information for Business Card

Company name, VelaShield
Logo, VS

Garth Ormsby
velashieldnz@postkite.example
+64219302648
www.velashield.example.nz

Requirements
Must have
• Simple clean look.
Nice to have
• We apply nano coatings so try and incorporate this into a theme somehow

```html
<!DOCTYPE html>
<html lang="en">
<head>
<meta charset="UTF-8">
<title>Vela Shield – Business Cards</title>
<link href="https://fonts.googleapis.com/css2?family=Open+Sans:wght@400;600;700&display=swap" rel="stylesheet">
<style>
  :root {
    --backdrop: #e4e4e4;
    --card-dark: #414042;
    --card-light: #ffffff;
    --brand-green: #6aad3d;
    --ink: #2e2e2e;
    --ink-soft: #555555;
    --ghost: #ececec;
    --marker: #3f3f3f;
  }
  * { margin: 0; padding: 0; box-sizing: border-box; }
  html, body {
    width: 1200px; height: 850px; overflow: hidden;
    background: var(--backdrop);
    font-family: "Open Sans", Arial, sans-serif;
  }
  .canvas { position: relative; width: 1200px; height: 850px; }

  .card {
    position: absolute;
    width: 540px; height: 310px;
    box-shadow: 0 10px 28px rgba(0,0,0,0.22);
    overflow: hidden;
  }

  /* Front */
  .card-front {
    left: 50px; top: 130px;
    background: var(--card-dark);
    display: flex; align-items: center; justify-content: center;
  }
  .brand-mark {
    display: flex; align-items: center; gap: 14px;
  }
  .brand-dot {
    width: 34px; height: 34px; border-radius: 50%;
    background: var(--brand-green);
  }
  .card-front .brand-name {
    color: var(--brand-green);
    font-size: 44px; font-weight: 600; letter-spacing: -0.5px;
  }

  /* Back */
  .card-back {
    left: 610px; top: 410px;
    background: var(--card-light);
  }
  .card-back .brand-mark {
    position: absolute; top: 36px; right: 36px; gap: 10px;
  }
  .card-back .brand-dot { width: 24px; height: 24px; background: var(--ink); }
  .card-back .brand-name {
    color: var(--ink); font-size: 28px; font-weight: 600; letter-spacing: -0.3px;
  }
  .ghost-name {
    position: absolute; right: -10px; bottom: 24px;
    font-size: 66px; font-weight: 600; color: var(--ghost);
    letter-spacing: -1px; white-space: nowrap;
  }
  .side-marker {
    position: absolute; left: 0; top: 118px;
    width: 12px; height: 30px; background: var(--marker);
  }
  .holder { position: absolute; left: 32px; top: 104px; }
  .holder-name { font-size: 21px; font-weight: 700; color: var(--ink); line-height: 1.2; }
  .holder-role { font-size: 13px; color: var(--ink-soft); }
  .tagline {
    position: absolute; left: 32px; top: 172px;
    font-size: 13px; font-weight: 700; color: var(--ink);
  }
  .contacts {
    position: absolute; left: 32px; top: 212px;
    list-style: none;
  }
  .contacts li {
    display: flex; align-items: center; gap: 8px;
    font-size: 13px; color: var(--ink); margin-bottom: 6px;
  }
  .contacts svg { width: 18px; height: 18px; flex: none; }
</style>
</head>
<body>
<div class="canvas">

  <section class="card card-front">
    <div class="brand-mark">
      <span class="brand-dot"></span>
      <span class="brand-name">Vela Shield</span>
    </div>
  </section>

  <section class="card card-back">
    <div class="ghost-name" aria-hidden="true">Vela Shield</div>

    <div class="brand-mark">
      <span class="brand-dot"></span>
      <span class="brand-name">Vela Shield</span>
    </div>

    <span class="side-marker"></span>
    <div class="holder">
      <p class="holder-name">Garth Ormsby</p>
      <p class="holder-role">Managing Director</p>
    </div>

    <p class="tagline">Antimicrobial Surface Protection</p>

    <ul class="contacts">
      <li>
        <svg viewBox="0 0 20 20" aria-hidden="true"><circle cx="10" cy="10" r="9" fill="none" stroke="#2e2e2e" stroke-width="1.4"/><path d="M7 5.5l2 2-1 1.2a6 6 0 0 0 3.3 3.3l1.2-1 2 2-1.3 1.5C9.6 14.3 5.7 10.4 5.5 6.8z" fill="#2e2e2e"/></svg>
        +64219302648
      </li>
      <li>
        <svg viewBox="0 0 20 20" aria-hidden="true"><circle cx="10" cy="10" r="9" fill="none" stroke="#2e2e2e" stroke-width="1.4"/><rect x="5" y="6.5" width="10" height="7" fill="#2e2e2e"/><path d="M5 6.5l5 4 5-4" fill="none" stroke="#fff" stroke-width="1"/></svg>
        velashieldnz@postkite.example
      </li>
      <li>
        <svg viewBox="0 0 20 20" aria-hidden="true"><circle cx="10" cy="10" r="9" fill="none" stroke="#2e2e2e" stroke-width="1.4"/><circle cx="10" cy="10" r="5.5" fill="none" stroke="#2e2e2e" stroke-width="1"/><ellipse cx="10" cy="10" rx="2.3" ry="5.5" fill="none" stroke="#2e2e2e" stroke-width="1"/><path d="M4.5 10h11" stroke="#2e2e2e" stroke-width="1"/></svg>
        www.velashield.example.nz
      </li>
    </ul>
  </section>

</div>
</body>
</html>
```